Business Card Design for a Lending Business (Hard Money loans)

We need a business card for our Real Estate Lending business. We do hard Money loans for real estate investors. We have an existing logo we like, see attached. I'd like the business card to mostly include the logo colors, but a bright color pop of some sort would be nice to see also. Card should include Logo, Company Name, Company Address, Employee Name, Cell Phone, Main Phone, Email, Website

Industry/Entity Type

Finance / Lending

Contact Information for Business Card

Logo, Company Name, Company Address, Employee Name, Cell Phone, Main Phone, Email, Website

Requirements
Nice to have
• I'd like the business card to mostly include the logo colors, but a bright color pop of some sort would be nice to see also.

```html
<!DOCTYPE html>
<html lang="en">
<head>
<meta charset="utf-8">
<title>Ringroute Lending – Business Card</title>
<link href="https://fonts.googleapis.com/css2?family=Lato:wght@400;700;900&display=swap" rel="stylesheet">
<style>
  :root {
    --stage: #2a2a2a;
    --paper: #ffffff;
    --navy: #00288a;
    --sky: #1aa8e0;
    --ink: #1c1c24;
  }
  * { box-sizing: border-box; margin: 0; padding: 0; }
  html, body { width: 1200px; height: 1000px; overflow: hidden; }
  body {
    background: var(--stage);
    font-family: "Lato", sans-serif;
    position: relative;
  }
  .card {
    position: absolute;
    left: 303px;
    width: 591px;
    height: 340px;
    border-radius: 17px;
    overflow: hidden;
  }
  .card-front { top: 126px; background: var(--paper); }
  .card-back { top: 537px; background: var(--navy); display: flex; align-items: center; justify-content: center; }

  .brand { display: flex; align-items: center; gap: 10px; font-family: "Lato", sans-serif; font-weight: 900; letter-spacing: 2px; }
  .brand-front { position: absolute; left: 37px; top: 60px; color: var(--navy); font-size: 19px; }
  .brand-front .brand-dot { width: 34px; height: 34px; border-radius: 50%; background: var(--navy); }
  .brand-back { flex-direction: column; gap: 22px; color: #ffffff; font-size: 30px; letter-spacing: 4px; }
  .brand-back .brand-dot { width: 90px; height: 90px; border-radius: 50%; background: var(--sky); }

  .person { position: absolute; left: 37px; top: 214px; }
  .person-name { color: var(--sky); font-weight: 900; font-size: 23px; letter-spacing: 0.5px; line-height: 1; }
  .person-role { color: var(--ink); font-size: 14px; margin-top: 6px; }

  .contact-list { position: absolute; left: 263px; top: 194px; list-style: none; }
  .contact-list li { display: flex; align-items: center; gap: 8px; font-size: 14px; color: var(--ink); height: 19.5px; }
  .contact-list svg { width: 12px; height: 12px; fill: var(--navy); flex: none; }

  .divider { position: absolute; left: 37px; top: 280px; width: 519px; height: 1.5px; background: var(--sky); }

  .address { position: absolute; left: 263px; top: 286px; display: flex; align-items: center; gap: 8px; font-size: 14px; color: var(--ink); }
  .address svg { width: 12px; height: 12px; fill: var(--navy); }
</style>
</head>
<body>
  <section class="card card-front">
    <div class="brand brand-front"><span class="brand-dot"></span><span class="brand-name">RINGROUTE LENDING</span></div>

    <div class="person">
      <p class="person-name">DANA WHITFIELD</p>
      <p class="person-role">Manager</p>
    </div>

    <ul class="contact-list">
      <li><svg viewBox="0 0 12 12"><path d="M3 0h6a1 1 0 0 1 1 1v10a1 1 0 0 1-1 1H3a1 1 0 0 1-1-1V1a1 1 0 0 1 1-1zm0 1.5v8h6v-8zM6 10.2a.6.6 0 1 0 0 1.2.6.6 0 0 0 0-1.2z"/></svg>555-014-2210</li>
      <li><svg viewBox="0 0 12 12"><path d="M2.5 0.8 4.3 3 3.4 4.3a7 7 0 0 0 4.3 4.3L9 7.7l2.2 1.8-1 1.9C5.4 11.4.6 6.6.6 1.8z"/></svg>555-014-3380</li>
      <li><svg viewBox="0 0 12 12"><path d="M0 2h12v1.2L6 7 0 3.2zm0 2.6 6 3.8 6-3.8V10H0z"/></svg>hello@ringroutelending.com</li>
      <li><svg viewBox="0 0 12 12"><path d="M6 0a6 6 0 1 0 0 12A6 6 0 0 0 6 0zm-1 2 1.5 1.5L5 5 3 4.5 2 3A4.5 4.5 0 0 1 5 2zm3 3 2 .5A4.5 4.5 0 0 1 7 10.3L7.5 8 6 6.5z"/></svg>www.ringroutelending.com</li>
    </ul>

    <div class="divider"></div>

    <p class="address"><svg viewBox="0 0 12 12"><path d="M6 0a4 4 0 0 1 4 4c0 3-4 8-4 8S2 7 2 4a4 4 0 0 1 4-4zm0 2.4a1.6 1.6 0 1 0 0 3.2 1.6 1.6 0 0 0 0-3.2z"/></svg>1820 Larkspur Lane, Fairhaven, MD 20779</p>
  </section>

  <section class="card card-back">
    <div class="brand brand-back"><span class="brand-dot"></span><span class="brand-name">RINGROUTE LENDING</span></div>
  </section>
</body>
</html>
```